International Automotive Parts Marketing business needs professional, sleek Android app design.

We have developed an Android app for our sales team and are now looking for an overall design our developers can apply. The design should mirror our corporate website kvelora.com. There is a LOT of data the reps need to work through so not really any images other that login screen - of course icons are great. Lots of lists and searches etc. - it needs to look professional, feel amazing and easy to use. Our motto - Simple is always better. We included our logo and a few screenshots of the app page 1 and 2.

Target Market(s)

Professional Sales and Marketing - our own sales team (100 reps) will use this app

Font styles to use
Sans Serif

Colors

Designer to choose colors to be used in the design.

Requirements
Must have
• App design must be professional and easy to use in the field all day. Similar look and feel of corporate website kvelora.com. Same colors and images. Icons to manage navigation
Should not have
• Non-professional look and feel. No vector cartoon type images. No specific parts related images

```html
<!DOCTYPE html>
<html lang="en">
<head>
<meta charset="utf-8">
<title>Kvelora Parts — Navigation Drawer</title>
<link href="https://fonts.googleapis.com/css2?family=Nunito+Sans:wght@400;600;800&display=swap" rel="stylesheet">
<style>
  :root {
    --drawer: #000000;
    --backdrop: #202020;
    --ink: #ffffff;
    --brand-red: #b51a33;
  }
  * { margin: 0; padding: 0; box-sizing: border-box; }
  html, body { width: 675px; height: 1200px; overflow: hidden; background: var(--backdrop); }
  body { font-family: "Nunito Sans", Arial, sans-serif; color: var(--ink); }
  .screen { position: relative; width: 675px; height: 1200px; overflow: hidden; background: var(--backdrop); }
  .drawer-shape { position: absolute; inset: 0; }
  .status-bar { position: absolute; top: 0; left: 0; right: 0; height: 44px; }
  .status-time { position: absolute; left: 21px; top: 9px; font-size: 19px; font-weight: 600; letter-spacing: 0.2px; }
  .status-icons { position: absolute; right: 20px; top: 12px; }
  .brand { position: absolute; left: 35px; top: 64px; display: flex; align-items: center; gap: 14px; }
  .brand-dot { width: 82px; height: 82px; border-radius: 50%; background: var(--brand-red); }
  .brand-name { font-size: 30px; font-weight: 800; letter-spacing: 1px; text-transform: uppercase; color: var(--ink); }
  .menu { position: absolute; left: 0; top: 0; list-style: none; }
  .menu-item { position: absolute; left: 48px; width: 330px; height: 80px; display: flex; align-items: center; transform: translateY(-40px); }
  .menu-icon { width: 76px; height: 76px; flex: none; }
  .menu-label { margin-left: 37px; font-size: 22.5px; font-weight: 400; }
  .collapse-btn { position: absolute; left: 415px; top: 228px; width: 66px; height: 66px; border-radius: 50%; background: var(--drawer); display: flex; align-items: center; justify-content: center; }
</style>
</head>
<body>
<main class="screen">
  <svg class="drawer-shape" width="675" height="1200" viewBox="0 0 675 1200" aria-hidden="true">
    <path d="M0 0 H446 V160 C446 200 399 205 399 261 C399 317 446 322 446 362 V1200 H0 Z" fill="var(--drawer)"/>
  </svg>

  <div class="status-bar">
    <span class="status-time">9:41</span>
    <svg class="status-icons" width="96" height="18" viewBox="0 0 96 18" aria-hidden="true">
      <g fill="#fff">
        <rect x="0" y="11" width="3.5" height="5" rx="1"/>
        <rect x="5.5" y="8" width="3.5" height="8" rx="1"/>
        <rect x="11" y="5" width="3.5" height="11" rx="1"/>
        <rect x="16.5" y="1" width="3.5" height="15" rx="1"/>
      </g>
      <g fill="none" stroke="#fff" stroke-width="2.2" stroke-linecap="round">
        <path d="M28 6 A13 13 0 0 1 46 6"/>
        <path d="M31 9.5 A8 8 0 0 1 43 9.5"/>
      </g>
      <circle cx="37" cy="14" r="2.3" fill="#fff"/>
      <rect x="58" y="1" width="33" height="15" rx="4" fill="none" stroke="#fff" stroke-width="1.6"/>
      <rect x="61" y="4" width="27" height="9" rx="2" fill="#fff"/>
      <rect x="92.5" y="6" width="2.5" height="5" rx="1" fill="#fff"/>
    </svg>
  </div>

  <div class="brand">
    <span class="brand-dot"></span>
    <span class="brand-name">Kvelora Parts</span>
  </div>

  <div class="collapse-btn">
    <svg width="28" height="24" viewBox="0 0 28 24" aria-label="Collapse menu" role="img">
      <g fill="none" stroke="#fff" stroke-width="3" stroke-linecap="round" stroke-linejoin="round">
        <path d="M13 3 L4 12 L13 21"/>
        <path d="M24 3 L15 12 L24 21"/>
      </g>
    </svg>
  </div>

  <ul class="menu">
    <li class="menu-item" style="top:256px">
      <svg class="menu-icon" viewBox="0 0 76 76" aria-hidden="true">
        <g fill="none" stroke="#fff" stroke-width="2.2" stroke-linecap="round">
          <path d="M60 4 a8 8 0 0 1 8 8 c0 7 -8 14 -8 14 c0 0 -8 -7 -8 -14 a8 8 0 0 1 8 -8z"/>
          <circle cx="60" cy="12" r="3"/>
          <path d="M14 30 a10 10 0 0 1 10 10 c0 9 -10 18 -10 18 c0 0 -10 -9 -10 -18 a10 10 0 0 1 10 -10z"/>
          <circle cx="14" cy="40" r="4"/>
          <path d="M52 28 H42 a6 6 0 0 0 0 12 H66 a6 6 0 0 1 0 12 H40 a7 7 0 0 0 0 14 H70" stroke-dasharray="3 3"/>
        </g>
      </svg>
      <span class="menu-label">Route</span>
    </li>
    <li class="menu-item" style="top:390px">
      <svg class="menu-icon" viewBox="0 0 76 76" aria-hidden="true">
        <g fill="none" stroke="#fff" stroke-width="2.4" stroke-linecap="round">
          <circle cx="30" cy="30" r="22"/>
          <circle cx="30" cy="30" r="17"/>
          <path d="M46 46 L52 52"/>
          <path d="M51 49 L67 65 a3 3 0 0 1 -4 4 L47 53 Z"/>
        </g>
      </svg>
      <span class="menu-label">Search</span>
    </li>
    <li class="menu-item" style="top:524px">
      <svg class="menu-icon" viewBox="0 0 76 76" aria-hidden="true">
        <g fill="none" stroke="#fff" stroke-width="2.2" stroke-linejoin="round">
          <circle cx="22" cy="11" r="5"/><circle cx="38" cy="11" r="5"/><circle cx="54" cy="11" r="5"/>
          <path d="M13 30 v-6 a5 5 0 0 1 5 -5 h8 a5 5 0 0 1 5 5 v6"/>
          <path d="M29 30 v-6 a5 5 0 0 1 5 -5 h8 a5 5 0 0 1 5 5 v6"/>
          <path d="M45 30 v-6 a5 5 0 0 1 5 -5 h8 a5 5 0 0 1 5 5 v6"/>
          <path d="M11 30 H65"/>
          <path d="M20 50 l10 -8 h14 a4 4 0 0 1 0 8 h-10 M44 50 l16 -10 a4 4 0 0 1 5 6 l-20 15 H28 l-4 3"/>
          <path d="M4 60 l12 -12 l12 12 l-12 12 z"/>
        </g>
      </svg>
      <span class="menu-label">Custom List</span>
    </li>
    <li class="menu-item" style="top:658px">
      <svg class="menu-icon" viewBox="0 0 76 76" aria-hidden="true">
        <g fill="none" stroke="#fff" stroke-width="2.2" stroke-linecap="round" stroke-linejoin="round">
          <circle cx="38" cy="18" r="5"/>
          <path d="M38 6 v3 M38 27 v3 M26 18 h3 M47 18 h3 M30 10 l2 2 M44 24 l2 2 M30 26 l2 -2 M44 12 l2 -2"/>
          <circle cx="38" cy="18" r="9"/>
          <path d="M38 32 v30" stroke-dasharray="3 3"/>
          <circle cx="23" cy="42" r="7"/><circle cx="53" cy="42" r="7"/>
          <path d="M6 72 v-10 a11 11 0 0 1 11 -11 h12 a11 11 0 0 1 6 3"/>
          <path d="M70 72 v-10 a11 11 0 0 0 -11 -11 h-12 a11 11 0 0 0 -6 3"/>
          <path d="M14 64 v8 M62 64 v8"/>
        </g>
      </svg>
      <span class="menu-label">Partner</span>
    </li>
    <li class="menu-item" style="top:792px">
      <svg class="menu-icon" viewBox="0 0 76 76" aria-hidden="true">
        <g fill="none" stroke="#fff" stroke-width="2.2" stroke-linecap="round">
          <circle cx="38" cy="38" r="12"/>
          <circle cx="38" cy="34" r="4"/>
          <path d="M30 46 a9 8 0 0 1 16 0"/>
          <circle cx="38" cy="6" r="5"/><circle cx="38" cy="70" r="5"/>
          <circle cx="10" cy="22" r="5"/><circle cx="66" cy="22" r="5"/>
          <circle cx="10" cy="54" r="5"/><circle cx="66" cy="54" r="5"/>
          <path d="M38 11 v15 M38 50 v15 M14 24 l13 8 M62 24 l-13 8 M14 52 l13 -8 M62 52 l-13 -8" stroke-dasharray="2 3"/>
          <path d="M10 27 v22 M66 27 v22 M14 19 l19 -11 M62 19 l-19 -11 M14 57 l19 11 M62 57 l-19 11" stroke-dasharray="2 3"/>
        </g>
      </svg>
      <span class="menu-label">Market Touches</span>
    </li>
    <li class="menu-item" style="top:926px">
      <svg class="menu-icon" viewBox="0 0 76 76" aria-hidden="true">
        <g fill="none" stroke="#fff" stroke-width="2.4" stroke-linejoin="round">
          <path d="M24 28 h8 l2 6 l6 3 l6 -3 l5 5 l-3 6 l3 6 l6 2 v8 l-6 2 l-3 6 l3 6 l-5 5 l-6 -3 l-6 3 l-2 6 h-8 l-2 -6 l-6 -3 l-6 3 l-5 -5 l3 -6 l-3 -6 l-6 -2 v-8 l6 -2 l3 -6 l-3 -6 l5 -5 l6 3 l6 -3 z" transform="translate(0 -4) scale(0.82) translate(3 10)"/>
          <circle cx="27" cy="49" r="7"/>
          <path d="M54 4 h6 l1 4 l4 2 l4 -2 l4 4 l-2 4 l2 4 l4 1 v6 l-4 1 l-2 4 l2 4 l-4 4 l-4 -2 l-4 2 l-1 4 h-6 l-1 -4 l-4 -2 l-4 2 l-4 -4 l2 -4 l-2 -4 l-4 -1 v-6 l4 -1 l2 -4 l-2 -4 l4 -4 l4 2 l4 -2 z" transform="translate(10 4) scale(0.8)"/>
          <circle cx="56" cy="22" r="4.5"/>
        </g>
      </svg>
      <span class="menu-label">Settings</span>
    </li>
  </ul>
</main>
</body>
</html>
```